Business Cards

Business card design for my company.
I would like the card's background colour to be black. You can also see our web site to get an idea of our brand. https://www.dlqmarrowfield.com.au/
- Name
- Email

```html
<!DOCTYPE html>
<html lang="en">
<head>
<meta charset="utf-8">
<title>DLQ Marrowfield – Business Cards</title>
<link href="https://fonts.googleapis.com/css2?family=Barlow:wght@700&family=Montserrat:wght@400&display=swap" rel="stylesheet">
<style>
  :root {
    --page-bg: #2b2b2b;
    --card-black: #070707;
    --card-sheen: #1c1c1c;
    --brand-white: #ffffff;
    --brand-green: #1fa64a;
    --badge-blue: #2f5fb3;
    --badge-dark: #3a3a3a;
    --badge-orange: #f2a81d;
    --badge-silver: #c9c9c9;
    --badge-gold: #c9a43c;
  }
  * { box-sizing: border-box; margin: 0; padding: 0; }
  html, body { width: 1200px; height: 886px; overflow: hidden; }
  body {
    background: var(--page-bg);
    display: flex;
    flex-direction: column;
    align-items: center;
    justify-content: center;
    gap: 26px;
  }
  .card {
    position: relative;
    width: 620px;
    height: 390px;
    border-radius: 22px;
    background:
      linear-gradient(125deg, transparent 0 38%, var(--card-sheen) 38% 39%, transparent 60%),
      linear-gradient(160deg, #141414 0%, var(--card-black) 55%, #000 100%);
    box-shadow: 0 14px 30px rgba(0,0,0,.55);
    display: flex;
    flex-direction: column;
    align-items: center;
    overflow: hidden;
  }
  .brand-name {
    font-family: "Barlow", sans-serif;
    font-weight: 700;
    color: var(--brand-white);
    font-size: 46px;
    letter-spacing: 4px;
    line-height: 1;
  }
  .brand-rule {
    width: 110px;
    height: 3px;
    background: var(--brand-green);
    margin-top: 26px;
  }
  .card--front .brand-name { margin-top: 110px; }
  .badge-row {
    display: flex;
    gap: 12px;
    margin-top: 70px;
  }
  .badge {
    width: 50px;
    height: 50px;
    border-radius: 50%;
    border: 2px solid rgba(255,255,255,.7);
  }
  .badge--blue { background: var(--badge-blue); border-color: #fff; }
  .badge--dark { background: var(--badge-dark); }
  .badge--orange { background: var(--badge-orange); border-color: var(--badge-orange); }
  .badge--silver { background: var(--badge-silver); }
  .badge--gold { background: var(--badge-gold); border-color: var(--badge-gold); }
  .card--back .brand-name { margin-top: 90px; }
  .holder-name {
    margin-top: 38px;
    font-family: "Barlow", sans-serif;
    font-weight: 700;
    font-size: 32px;
    color: var(--brand-white);
    letter-spacing: .5px;
  }
  .contact {
    font-family: "Montserrat", sans-serif;
    font-weight: 400;
    font-size: 21px;
    line-height: 1.4;
    text-align: center;
    margin-top: 6px;
  }
  .contact__email { color: var(--brand-white); }
  .contact__web { color: var(--brand-green); }
</style>
</head>
<body>
  <section class="card card--front">
    <div class="brand-name">DLQ MARROWFIELD</div>
    <div class="brand-rule"></div>
    <div class="badge-row" aria-label="Industry award badges">
      <span class="badge badge--blue"></span>
      <span class="badge badge--dark"></span>
      <span class="badge badge--orange"></span>
      <span class="badge badge--silver"></span>
      <span class="badge badge--gold"></span>
      <span class="badge badge--dark"></span>
      <span class="badge badge--silver"></span>
      <span class="badge badge--gold"></span>
      <span class="badge badge--dark"></span>
    </div>
  </section>

  <section class="card card--back">
    <div class="brand-name">DLQ MARROWFIELD</div>
    <div class="brand-rule"></div>
    <div class="holder-name">YOUR NAME HERE</div>
    <div class="contact">
      <div class="contact__email">youremail@dlqmarrowfield.com.au</div>
      <div class="contact__web">www.dlqmarrowfield.com.au</div>
    </div>
  </section>
</body>
</html>
```